Business Card Design Project

Hi,
This is a simple contest. The logo for the back of the card is deigned. See attached files. The front of the card must have :

Directors Name: Dorian
Mob:
e-mail:
Postal Address:
Web Page Adress:

It may also add words: "Leaders in Construction Project Management Services"

Target Market(s)

Business & Home owners alike

Industry/Entity Type

Business

Requirements
Must have
• See details above and logo attached
Should not have
• Images other than logo

```html
<!DOCTYPE html>
<html lang="en">
<head>
<meta charset="utf-8">
<title>Meridian Projects Australia – Business Card</title>
<link rel="stylesheet" href="https://fonts.googleapis.com/css2?family=PT+Sans:ital,wght@0,400;0,700;1,400&family=Arimo:wght@400&display=swap">
<style>
  :root {
    --stage: #3b3b3d;
    --label: #d6d6d6;
    --brand-blue: #0098da;
    --card-white: #ffffff;
    --ink: #1c1c1c;
    --font-main: "PT Sans", sans-serif;
    --font-mail: "Arimo", sans-serif;
  }
  * { margin: 0; padding: 0; box-sizing: border-box; }
  html, body { width: 993px; height: 1200px; overflow: hidden; }
  body {
    position: relative;
    background: var(--stage);
    font-family: var(--font-main);
  }
  .side-label {
    position: absolute;
    left: 90px;
    color: var(--label);
    font-size: 23px;
  }
  .side-label--front { top: 46px; }
  .side-label--back { top: 599px; }

  .card {
    position: absolute;
    left: 95px;
    width: 812px;
    height: 470px;
    overflow: hidden;
    box-shadow: 0 2px 6px rgba(0,0,0,.45);
  }
  .card--front { top: 95px; background: var(--card-white); }
  .card--back { top: 659px; background: var(--brand-blue); }

  /* Front */
  .brand-band {
    position: absolute;
    right: 0; top: 0;
    width: 180px; height: 100%;
    background: var(--brand-blue);
  }
  .brand-band__name {
    position: absolute;
    left: 0; right: 0;
    top: 213px;
    display: flex;
    align-items: center;
    justify-content: center;
    gap: 10px;
    color: var(--card-white);
    font-weight: 700;
    font-size: 24px;
    letter-spacing: 1px;
  }
  .brand-band__square {
    width: 14px; height: 14px;
    background: var(--card-white);
  }
  .identity {
    position: absolute;
    left: 0; width: 628px;
    top: 44px;
    text-align: center;
  }
  .identity__name {
    color: var(--brand-blue);
    font-weight: 700;
    font-size: 39px;
    line-height: 1;
  }
  .identity__role {
    margin-top: 6px;
    font-style: italic;
    font-size: 28px;
    color: var(--ink);
    line-height: 1.1;
  }
  .identity__email {
    margin-top: 6px;
    font-family: var(--font-mail);
    font-size: 24px;
    color: var(--ink);
  }
  .tagline {
    position: absolute;
    left: 0; top: 203px;
    width: 628px; height: 52px;
    background: var(--brand-blue);
    color: var(--card-white);
    font-size: 23px;
    line-height: 52px;
    padding-left: 36px;
  }
  .contact {
    position: absolute;
    top: 313px;
    font-size: 23px;
    line-height: 32px;
    color: var(--ink);
  }
  .contact--postal { left: 36px; }
  .contact--direct { right: 209px; text-align: right; }

  /* Back */
  .lockup {
    position: absolute;
    left: 0; right: 0;
    top: 168px;
    display: flex;
    align-items: center;
    justify-content: center;
    gap: 22px;
    color: var(--card-white);
    font-weight: 700;
  }
  .lockup__square {
    width: 60px; height: 60px;
    background: var(--card-white);
  }
  .lockup__text { line-height: 1; }
  .lockup__name { font-size: 64px; letter-spacing: 1px; }
  .lockup__sub { font-size: 22px; letter-spacing: 6px; margin-top: 4px; }
  .back-web {
    position: absolute;
    left: 0; right: 0;
    top: 393px;
    text-align: center;
    color: var(--card-white);
    font-size: 23px;
  }
</style>
</head>
<body>
  <div class="side-label side-label--front">Front</div>
  <section class="card card--front">
    <div class="brand-band">
      <div class="brand-band__name"><span class="brand-band__square"></span>MERIDIAN</div>
    </div>
    <div class="identity">
      <div class="identity__name">Dorian</div>
      <div class="identity__role">Directors</div>
      <div class="identity__email">Dorian@meridianbusiness.com</div>
    </div>
    <div class="tagline">Leaders in Construction Project Management Services</div>
    <address class="contact contact--postal" style="font-style:normal">
      4170 harbour road<br>West Harbour, BC<br>K3P 418
    </address>
    <div class="contact contact--direct">
      phone: (03541) 5550142<br>www.meridianbusiness.com
    </div>
  </section>

  <div class="side-label side-label--back">Back</div>
  <section class="card card--back">
    <div class="lockup">
      <span class="lockup__square"></span>
      <div class="lockup__text">
        <div class="lockup__name">MERIDIAN</div>
        <div class="lockup__sub">PROJECTS AUSTRALIA</div>
      </div>
    </div>
    <div class="back-web">www.meridianbusiness.com</div>
  </section>
</body>
</html>
```